Hot Consulting firm collateral upgrade

We need a stationary design for our Oakland based consulting company called Travilux. We provide consulting expertise in KRB compliance for Medical Device, Pharmaceutical, and Biotech companies. We will be using the stationary for all of our marketing collateral. We want the design to convey professionalism and quality. You can find our company color scheme from our website travilux-example.com. I have included a copy of our current stationary that needs an upgrade.
Target Market(s)
Medical Device, Pharma, and Biotech companies
Industry/Entity Type
It Company
Look and feel

```html
<!DOCTYPE html>
<html lang="en">
<head>
<meta charset="utf-8">
<title>Travilux Letterhead</title>
<link href="https://fonts.googleapis.com/css2?family=PT+Sans:wght@400&display=swap" rel="stylesheet">
<style>
  :root {
    --brand-blue: #17609e;
    --accent-grey: #a7aab0;
    --paper: #ffffff;
    --backdrop: #ffffff;
    --ink-light: #ffffff;
  }
  html, body {
    margin: 0;
    padding: 0;
    width: 1200px;
    height: 1000px;
    overflow: hidden;
    background: var(--backdrop);
  }
  .canvas {
    position: relative;
    width: 1200px;
    height: 1000px;
  }
  .letterhead {
    position: absolute;
    left: 294px;
    top: 104px;
    width: 612px;
    height: 792px;
    background: var(--paper);
    box-shadow: 0 3px 10px rgba(0, 0, 0, 0.35);
    overflow: hidden;
  }
  .letterhead__bands {
    position: absolute;
    inset: 0;
    width: 612px;
    height: 792px;
  }
  .band-fill { fill: var(--brand-blue); }
  .band-line { fill: none; stroke: var(--brand-blue); }
  .band-line--grey { fill: none; stroke: var(--accent-grey); }
  .band-line--white { fill: none; stroke: var(--paper); }
  .letterhead__brand {
    position: absolute;
    left: 36px;
    top: 36px;
    margin: 0;
    font-family: "PT Sans", sans-serif;
    font-weight: 400;
    font-size: 38px;
    line-height: 1;
    letter-spacing: 0.5px;
    color: var(--ink-light);
  }
  .letterhead__footer {
    position: absolute;
    right: 31px;
    top: 729px;
    margin: 0;
    text-align: right;
    font-family: "PT Sans", sans-serif;
    font-size: 10px;
    line-height: 16px;
    letter-spacing: 0.3px;
    color: var(--ink-light);
    white-space: nowrap;
  }
  .letterhead__footer span { display: block; }
</style>
</head>
<body>
<div class="canvas">
  <article class="letterhead">
    <svg class="letterhead__bands" viewBox="0 0 612 792" aria-hidden="true">
      <path class="band-fill" d="M0 0 H612 V30 Q380 100 0 96 Z"/>
      <path class="band-line--grey" stroke-width="3" d="M0 98 Q380 102 612 32"/>
      <path class="band-line--white" stroke-width="1.5" d="M0 103 Q380 107 612 40"/>
      <path class="band-line" stroke-width="3.5" d="M0 108 Q380 111 612 47"/>
      <path class="band-line" stroke-width="3.5" d="M0 741 Q220 684 612 682"/>
      <path class="band-line--white" stroke-width="1.5" d="M0 746 Q220 690 612 688"/>
      <path class="band-fill" d="M0 749 Q220 693 612 691 V792 H0 Z"/>
      <path class="band-line--grey" stroke-width="2" d="M0 759 Q220 697 612 695"/>
    </svg>

    <h1 class="letterhead__brand">travilux</h1>

    <p class="letterhead__footer">
      <span>travilux-example.com &nbsp;|&nbsp; 555.014.2387 &nbsp;|&nbsp; © 2015 Travilux, inc.</span>
      <span>Oakland Bay Region &nbsp;|&nbsp; Fresno &nbsp;|&nbsp; Denver &nbsp;|&nbsp; Nevada &nbsp;|&nbsp; Atlanta</span>
    </p>
  </article>
</div>
</body>
</html>
```